Company Powerpoint template - Bold Kettle Works

I need a company powerpoint template for Bold Kettle Works that has a number of templated slides with an exciting supporting colour palette. Needs to have header and footer sections, tables in colour which support the logo colour, bar and line charts, dot point slides and image (placeholders) slides. Logo is attached.
The primary use of this template is to pitch for new work - ie about us page, previous clients page, then a breakdown of services offered in a table format with prices etc...

Target Market(s)

small to medium businesses - look is proessional, but edgy and exciting

Industry/Entity Type

Management Consulting

Font styles to use
Sans Serif

Requirements
Must have
• See project description.
Nice to have
• I like the use of gradient in colour
Should not have
• No drop shadow or 3d options - just clean flat design

```html
<!DOCTYPE html>
<html lang="en">
<head>
<meta charset="utf-8">
<title>Bold Kettle Works – Presentation Template Slides</title>
<link rel="stylesheet" href="https://fonts.googleapis.com/css2?family=Dosis:wght@400;500&family=Open+Sans:wght@400;600;700&display=swap">
<style>
  :root{
    --green:#9cc63b;
    --green-soft:#b5d66a;
    --blue:#33a7d6;
    --orange:#e0562f;
    --gold:#c9a63a;
    --ink:#141414;
    --text:#333333;
    --muted:#9a9a9a;
    --rule:#e6e6e6;
    --paper:#ffffff;
  }
  *{margin:0;padding:0;box-sizing:border-box}
  html,body{width:980px;height:1200px;overflow:hidden;background:var(--paper)}
  body{position:relative;font-family:"Open Sans",sans-serif}
  .slide{position:absolute;width:320px;height:180px;background:var(--paper);outline:1px solid var(--rule);font-family:"Open Sans",sans-serif}
  .col-1{left:3px}.col-2{left:330px}.col-3{left:656px}
  .row-1{top:8px}.row-2{top:253px}.row-3{top:498px}.row-4{top:743px}.row-5{top:988px}
  .defs{position:absolute;width:0;height:0;overflow:hidden}

  .slide-title{font-family:"Dosis",sans-serif;font-size:13px;fill:var(--text)}
  .brand{font-family:"Open Sans",sans-serif;font-weight:700;font-size:5.5px;fill:var(--text)}
  .foot-note{font-size:2.8px;fill:#fff}
  .page-no{font-size:3px;fill:#888;text-anchor:middle}
  .lorem{font-size:3.4px;fill:var(--muted)}
  .lorem-w{font-size:3.2px;fill:rgba(255,255,255,.85)}
  .label{font-size:4.4px;fill:var(--text)}
  .label-b{font-size:5px;font-weight:700;fill:var(--text)}
  .head-sm{font-size:6.5px;fill:var(--text);font-weight:600}
  .mid{text-anchor:middle}
  .end{text-anchor:end}
  .on-dark{fill:#fff}
  .c-green{fill:var(--green)}.c-blue{fill:var(--blue)}.c-ink{fill:var(--ink)}
  .price{font-size:11px;fill:#fff;text-anchor:middle;font-family:"Dosis",sans-serif}
  .year{font-family:"Dosis",sans-serif;font-size:7.5px;fill:#fff;text-anchor:middle}
  .tiny-w{font-size:2.4px;fill:#fff;text-anchor:middle}
  .pct{font-family:"Dosis",sans-serif;font-size:8px;fill:#999}
  .big-w{font-family:"Dosis",sans-serif;fill:#fff}
</style>
</head>
<body>

<svg class="defs" aria-hidden="true">
  <defs>
    <linearGradient id="band-blue" x1="0" x2="1"><stop offset="0" stop-color="#2aa0d4"/><stop offset="1" stop-color="#3ab3df"/></linearGradient>
    <linearGradient id="band-green-blue" x1="0" x2="1"><stop offset="0" stop-color="#9cc63b"/><stop offset="1" stop-color="#2ea9d8"/></linearGradient>
    <linearGradient id="photo-green" x1="0" y1="0" x2="1" y2="1"><stop offset="0" stop-color="#8fbf4a"/><stop offset=".55" stop-color="#b7d88a"/><stop offset="1" stop-color="#6fc0b2"/></linearGradient>
    <linearGradient id="photo-office" x1="0" y1="0" x2="1" y2="1"><stop offset="0" stop-color="#d4dbe1"/><stop offset="1" stop-color="#8a9aa8"/></linearGradient>
    <linearGradient id="photo-portrait" x1="0" y1="0" x2="0" y2="1"><stop offset="0" stop-color="#d8d8d8"/><stop offset="1" stop-color="#8a8a8a"/></linearGradient>
    <linearGradient id="photo-contact" x1="0" x2="1"><stop offset="0" stop-color="#a6cf4d"/><stop offset=".6" stop-color="#6cc49a"/><stop offset="1" stop-color="#3ab6c6"/></linearGradient>
  </defs>
  <symbol id="slide-head" viewBox="0 0 392 220">
    <line x1="17" y1="41" x2="375" y2="41" stroke="#eeeeee" stroke-width=".6"/>
    <rect x="306" y="15" width="11" height="11" fill="#9cc63b"/>
    <text class="brand" x="320" y="23.5">BOLD KETTLE WORKS</text>
  </symbol>
  <symbol id="slide-foot" viewBox="0 0 392 220">
    <rect x="0" y="208" width="366" height="7" fill="#9cc63b"/>
    <text class="foot-note" x="4" y="212.6">© 2017 BOLD KETTLE WORKS all rights reserved</text>
    <rect x="366" y="208" width="12" height="7" fill="#eeeeee"/>
    <rect x="379" y="207" width="13" height="13" fill="#141414"/>
  </symbol>
  <symbol id="i-bars" viewBox="0 0 10 10"><rect x="1.5" y="6" width="1.7" height="2.6" fill="currentColor"/><rect x="4.2" y="4" width="1.7" height="4.6" fill="currentColor"/><rect x="6.9" y="2" width="1.7" height="6.6" fill="currentColor"/></symbol>
  <symbol id="i-search" viewBox="0 0 10 10"><circle cx="4.3" cy="4.3" r="2.6" fill="none" stroke="currentColor" stroke-width="1.2"/><line x1="6.2" y1="6.2" x2="8.6" y2="8.6" stroke="currentColor" stroke-width="1.4"/></symbol>
  <symbol id="i-tick" viewBox="0 0 10 10"><polyline points="2,5.2 4.2,7.4 8,2.8" fill="none" stroke="currentColor" stroke-width="1.4"/></symbol>
  <symbol id="i-gear" viewBox="0 0 10 10"><circle cx="5" cy="5" r="2.8" fill="none" stroke="currentColor" stroke-width="1.6" stroke-dasharray="1.4 .8"/><circle cx="5" cy="5" r="1" fill="currentColor"/></symbol>
  <symbol id="i-pen" viewBox="0 0 10 10"><line x1="2" y1="8" x2="8" y2="2" stroke="currentColor" stroke-width="1.6"/><circle cx="2.2" cy="7.8" r=".7" fill="currentColor"/></symbol>
  <symbol id="i-crown" viewBox="0 0 10 10"><path d="M1.5 7.5V3l2.3 2L5 2l1.2 3 2.3-2v4.5z" fill="currentColor"/></symbol>
  <symbol id="i-heart" viewBox="0 0 10 10"><path d="M5 8.6 1.6 5.2A2 2 0 0 1 5 2.9a2 2 0 0 1 3.4 2.3z" fill="currentColor"/></symbol>
  <symbol id="i-people" viewBox="0 0 10 10"><circle cx="3.3" cy="3.6" r="1.3" fill="currentColor"/><circle cx="6.7" cy="3.6" r="1.3" fill="currentColor"/><path d="M1 8c0-2 1-3 2.3-3S5.6 6 5.6 8zM4.4 8c0-2 1-3 2.3-3S9 6 9 8z" fill="currentColor"/></symbol>
  <symbol id="i-target" viewBox="0 0 10 10"><circle cx="5" cy="5" r="3.3" fill="none" stroke="currentColor" stroke-width="1"/><circle cx="5" cy="5" r="1.4" fill="currentColor"/></symbol>
  <symbol id="i-box" viewBox="0 0 10 10"><rect x="2" y="2.5" width="6" height="5" fill="none" stroke="currentColor" stroke-width="1"/><line x1="2" y1="4.3" x2="8" y2="4.3" stroke="currentColor" stroke-width=".8"/></symbol>
</svg>

<!-- 1 Multiple Column Area -->
<svg class="slide col-1 row-1" viewBox="0 0 392 220">
  <use href="#slide-head"/><use href="#slide-foot"/>
  <text class="slide-title" x="17" y="31">Multiple Column Area</text>
  <text class="page-no" x="372" y="213">31</text>
  <g>
    <circle cx="50" cy="67" r="8" fill="var(--ink)"/><use href="#i-gear" x="45" y="62" width="10" height="10" color="#fff"/>
    <circle cx="122" cy="67" r="8" fill="var(--green)"/><use href="#i-pen" x="117" y="62" width="10" height="10" color="#fff"/>
    <circle cx="194" cy="67" r="8" fill="var(--blue)"/><use href="#i-search" x="189" y="62" width="10" height="10" color="#fff"/>
    <circle cx="266" cy="67" r="8" fill="var(--green)"/><use href="#i-pen" x="261" y="62" width="10" height="10" color="#fff"/>
    <circle cx="338" cy="67" r="8" fill="var(--ink)"/><use href="#i-bars" x="333" y="62" width="10" height="10" color="#fff"/>
  </g>
  <g>
    <text class="label mid" x="50" y="85">Your Text Here</text>
    <text class="label mid c-green" x="122" y="85">Your Text Here</text>
    <text class="label mid c-blue" x="194" y="85">Your Text Here</text>
    <text class="label mid c-green" x="266" y="85">Your Text Here</text>
    <text class="label mid" x="338" y="85">Your Text Here</text>
    <text class="lorem mid" x="50" y="91">Lorem ipsum consectetur</text><text class="lorem mid" x="50" y="96">adipiscing elit</text>
    <text class="lorem mid" x="122" y="91">Lorem ipsum consectetur</text><text class="lorem mid" x="122" y="96">adipiscing elit</text>
    <text class="lorem mid" x="194" y="91">Lorem ipsum consectetur</text><text class="lorem mid" x="194" y="96">adipiscing elit</text>
    <text class="lorem mid" x="266" y="91">Lorem ipsum consectetur</text><text class="lorem mid" x="266" y="96">adipiscing elit</text>
    <text class="lorem mid" x="338" y="91">Lorem ipsum consectetur</text><text class="lorem mid" x="338" y="96">adipiscing elit</text>
  </g>
  <line x1="25" y1="117" x2="368" y2="117" stroke="#e2e2e2" stroke-width=".6"/>
  <text class="head-sm" x="27" y="139">Heading Goes Here</text>
  <text class="lorem" x="27" y="147">Lorem ipsum dolor sit amet, consectetur adipiscing elit, sed do</text>
  <text class="lorem" x="27" y="152">eiusmod tempor incididunt ut labore et commodo consequat dolore</text>
  <text class="lorem" x="27" y="157">magna aliqua.</text>
  <text class="lorem" x="27" y="170">Duis aute irure dolor in reprehenderit in voluptate velit esse cillum</text>
  <text class="lorem" x="27" y="175">dolore eu fugiat nulla pariatur.</text>
  <text class="head-sm" x="212" y="139">Heading Goes Here</text>
  <text class="lorem" x="212" y="147">Lorem ipsum dolor sit amet, consectetur adipiscing elit, sed do</text>
  <text class="lorem" x="212" y="152">eiusmod tempor incididunt ut labore et commodo consequat dolore</text>
  <text class="lorem" x="212" y="157">magna aliqua.</text>
  <text class="lorem" x="212" y="170">Duis aute irure dolor in reprehenderit in voluptate velit esse cillum</text>
  <text class="lorem" x="212" y="175">dolore eu fugiat nulla pariatur.</text>
</svg>

<!-- 2 Monthly Subscription -->
<svg class="slide col-2 row-1" viewBox="0 0 392 220">
  <use href="#slide-head"/>
  <text class="slide-title" x="28" y="33">Monthly Subscription</text>
  <rect x="0" y="108" width="392" height="112" fill="url(#band-blue)"/>
  <rect x="57" y="73" width="80" height="35" fill="var(--orange)"/>
  <rect x="57" y="108" width="80" height="72" fill="#fff"/>
  <rect x="147" y="60" width="99" height="48" fill="var(--green)"/>
  <rect x="147" y="108" width="99" height="82" fill="#fff"/>
  <rect x="256" y="73" width="80" height="35" fill="var(--gold)"/>
  <rect x="256" y="108" width="80" height="72" fill="#fff"/>
  <text class="price" x="97" y="94">$300</text><text class="tiny-w" x="97" y="101">per month</text>
  <text class="price" x="196" y="92">$900</text><text class="tiny-w" x="196" y="100">per month</text>
  <text class="price" x="296" y="94">$400</text><text class="tiny-w" x="296" y="101">per month</text>
  <g>
    <text class="lorem mid" x="97" y="125">Single Edition</text><line x1="65" y1="129" x2="129" y2="129" stroke="#eee" stroke-width=".4"/>
    <text class="lorem mid" x="97" y="139">20gb Cloud Service</text><line x1="65" y1="143" x2="129" y2="143" stroke="#eee" stroke-width=".4"/>
    <text class="lorem mid" x="97" y="153">3 User</text><line x1="65" y1="157" x2="129" y2="157" stroke="#eee" stroke-width=".4"/>
    <text class="lorem mid" x="97" y="168">Free Update</text>
    <text class="lorem mid" x="196" y="127">Business Edition</text><line x1="156" y1="132" x2="237" y2="132" stroke="#eee" stroke-width=".4"/>
    <text class="lorem mid" x="196" y="143">90gb Cloud Service</text><line x1="156" y1="148" x2="237" y2="148" stroke="#eee" stroke-width=".4"/>
    <text class="lorem mid" x="196" y="159">8 User</text><line x1="156" y1="164" x2="237" y2="164" stroke="#eee" stroke-width=".4"/>
    <text class="lorem mid" x="196" y="175">Free Update</text>
    <text class="lorem mid" x="296" y="125">Single Edition</text><line x1="264" y1="129" x2="328" y2="129" stroke="#eee" stroke-width=".4"/>
    <text class="lorem mid" x="296" y="139">20gb Cloud Service</text><line x1="264" y1="143" x2="328" y2="143" stroke="#eee" stroke-width=".4"/>
    <text class="lorem mid" x="296" y="153">3 User</text><line x1="264" y1="157" x2="328" y2="157" stroke="#eee" stroke-width=".4"/>
    <text class="lorem mid" x="296" y="168">Free Update</text>
  </g>
</svg>

<!-- 3 Divider -->
<svg class="slide col-3 row-1" viewBox="0 0 392 220">
  <rect x="0" y="0" width="392" height="220" fill="url(#photo-green)" role="img" aria-label="Photo of a hand writing with a pen, tinted green"/>
  <text class="tiny-w" x="81" y="117" style="text-anchor:start;font-size:4px">Divider Page</text>
  <text class="big-w" x="30" y="136" style="font-size:13px">Your Title Goes Here</text>
  <text class="big-w" x="65" y="150" style="font-size:6px;opacity:.85">Your Subtitle Here</text>
</svg>

<!-- 4 Video -->
<svg class="slide col-1 row-2" viewBox="0 0 392 220">
  <use href="#slide-head"/><use href="#slide-foot"/>
  <text class="page-no" x="372" y="213">34</text>
  <text class="slide-title" x="17" y="45" style="font-size:15px">Video Title</text>
  <text class="slide-title" x="17" y="61" style="font-size:15px">Goes Here</text>
  <text class="lorem" x="17" y="92">Lorem ipsum dolor sit amet, consectetur</text>
  <text class="lorem" x="17" y="97">adipiscing elit, sed do eiusmod tempor</text>
  <text class="lorem" x="17" y="102">incididunt ut labore et commodo</text>
  <text class="lorem" x="17" y="107">consequat dolore magna aliqua.</text>
  <text class="lorem" x="17" y="117">Duis aute irure dolor in reprehenderit in</text>
  <text class="lorem" x="17" y="122">voluptate velit esse cillum dolore eu</text>
  <text class="lorem" x="17" y="127">fugiat nulla pariatur.</text>
  <text class="lorem" x="17" y="137">Ut enimad minim veniam, quis nostrud</text>
  <text class="lorem" x="17" y="142">exercitation ullamco laboris.</text>
  <rect x="122" y="34" width="220" height="170" fill="url(#photo-office)" role="img" aria-label="Video placeholder: a desktop screen showing a person signing documents at a desk"/>
</svg>

<!-- 5 Four Column boxes -->
<svg class="slide col-2 row-2" viewBox="0 0 392 220">
  <use href="#slide-head"/><use href="#slide-foot"/>
  <text class="page-no" x="372" y="213">35</text>
  <text class="slide-title" x="17" y="31">Four Column Area</text>
  <text class="lorem" x="33" y="66">Lorem ipsum dolor sit amet, consectetur adipiscing elit, sed do eiusmod tempor incididunt ut labore et dolore magna aliqua.</text>
  <text class="lorem" x="33" y="72">Ut enimad minim veniam, quis nostrud exercitation ullamco laboris nisi ut aliquip ex ea commodo consequat.</text>
  <rect x="30" y="84" width="72" height="95" fill="var(--gold)"/>
  <rect x="117" y="84" width="72" height="95" fill="var(--blue)"/>
  <rect x="203" y="84" width="72" height="95" fill="var(--orange)"/>
  <rect x="289" y="84" width="72" height="95" fill="var(--green)"/>
  <circle cx="66" cy="111" r="8" fill="#fff"/><use href="#i-crown" x="62" y="107" width="8" height="8" color="var(--gold)"/>
  <circle cx="153" cy="111" r="8" fill="#fff"/><use href="#i-pen" x="149" y="107" width="8" height="8" color="var(--blue)"/>
  <circle cx="239" cy="111" r="8" fill="#fff"/><use href="#i-target" x="235" y="107" width="8" height="8" color="var(--orange)"/>
  <circle cx="325" cy="111" r="8" fill="#fff"/><use href="#i-bars" x="321" y="107" width="8" height="8" color="var(--green)"/>
  <g>
    <text class="lorem-w mid" x="66" y="143">YOUR TEXT HERE</text><text class="lorem-w mid" x="66" y="152">Lorem ipsum dolor sit</text><text class="lorem-w mid" x="66" y="157">amet consectetur</text><text class="lorem-w mid" x="66" y="162">adipiscing elit</text>
    <text class="lorem-w mid" x="153" y="143">YOUR TEXT HERE</text><text class="lorem-w mid" x="153" y="152">Lorem ipsum dolor sit</text><text class="lorem-w mid" x="153" y="157">amet consectetur</text><text class="lorem-w mid" x="153" y="162">adipiscing elit</text>
    <text class="lorem-w mid" x="239" y="143">YOUR TEXT HERE</text><text class="lorem-w mid" x="239" y="152">Lorem ipsum dolor sit</text><text class="lorem-w mid" x="239" y="157">amet consectetur</text><text class="lorem-w mid" x="239" y="162">adipiscing elit</text>
    <text class="lorem-w mid" x="325" y="143">YOUR TEXT HERE</text><text class="lorem-w mid" x="325" y="152">Lorem ipsum dolor sit</text><text class="lorem-w mid" x="325" y="157">amet consectetur</text><text class="lorem-w mid" x="325" y="162">adipiscing elit</text>
  </g>
</svg>

<!-- 6 Four Column rings -->
<svg class="slide col-3 row-2" viewBox="0 0 392 220">
  <use href="#slide-head"/><use href="#slide-foot"/>
  <text class="page-no" x="372" y="213">36</text>
  <text class="slide-title" x="17" y="31">Four Column Area</text>
  <text class="lorem mid" x="196" y="54">Lorem ipsum dolor sit amet, consectetur adipiscing elit, sed do eiusmod tempor incididunt ut labore et dolore magna aliqua. Ut enimad</text>
  <text class="lorem mid" x="196" y="60">minim veniam, quis nostrud exercitation ullamco laboris nisi ut aliquip ex ea commodo consequat.</text>
  <circle cx="77" cy="101" r="21" fill="none" stroke="var(--ink)" stroke-width="4"/><use href="#i-bars" x="69" y="93" width="16" height="16" color="var(--ink)"/>
  <circle cx="157" cy="101" r="21" fill="none" stroke="var(--blue)" stroke-width="4"/><use href="#i-crown" x="149" y="93" width="16" height="16" color="var(--blue)"/>
  <circle cx="236" cy="101" r="21" fill="none" stroke="var(--ink)" stroke-width="4"/><use href="#i-pen" x="228" y="93" width="16" height="16" color="var(--ink)"/>
  <circle cx="315" cy="101" r="21" fill="none" stroke="var(--green)" stroke-width="4"/><use href="#i-gear" x="307" y="93" width="16" height="16" color="var(--green)"/>
  <text class="label mid" x="77" y="141">COLUMN 1</text>
  <text class="label mid c-blue" x="157" y="141">COLUMN 2</text>
  <text class="label mid" x="236" y="141">COLUMN 3</text>
  <text class="label mid c-green" x="315" y="141">COLUMN 4</text>
  <g>
    <text class="lorem mid" x="77" y="149">Lorem ipsum dolor sit</text><text class="lorem mid" x="77" y="155">amet, consectetur</text><text class="lorem mid" x="77" y="161">adipiscing elit, sed do</text><text class="lorem mid" x="77" y="167">eiusmod tempor incididunt</text><text class="lorem mid" x="77" y="173">ut labore et dolore magna</text><text class="lorem mid" x="77" y="179">aliqua.</text>
    <text class="lorem mid" x="157" y="149">Lorem ipsum dolor sit</text><text class="lorem mid" x="157" y="155">amet, consectetur</text><text class="lorem mid" x="157" y="161">adipiscing elit, sed do</text><text class="lorem mid" x="157" y="167">eiusmod tempor incididunt</text><text class="lorem mid" x="157" y="173">ut labore et dolore magna</text><text class="lorem mid" x="157" y="179">aliqua.</text>
    <text class="lorem mid" x="236" y="149">Lorem ipsum dolor sit</text><text class="lorem mid" x="236" y="155">amet, consectetur</text><text class="lorem mid" x="236" y="161">adipiscing elit, sed do</text><text class="lorem mid" x="236" y="167">eiusmod tempor incididunt</text><text class="lorem mid" x="236" y="173">ut labore et dolore magna</text><text class="lorem mid" x="236" y="179">aliqua.</text>
    <text class="lorem mid" x="315" y="149">Lorem ipsum dolor sit</text><text class="lorem mid" x="315" y="155">amet, consectetur</text><text class="lorem mid" x="315" y="161">adipiscing elit, sed do</text><text class="lorem mid" x="315" y="167">eiusmod tempor incididunt</text><text class="lorem mid" x="315" y="173">ut labore et dolore magna</text><text class="lorem mid" x="315" y="179">aliqua.</text>
  </g>
</svg>

<!-- 7 Key Points -->
<svg class="slide col-1 row-3" viewBox="0 0 392 220">
  <use href="#slide-head"/><use href="#slide-foot"/>
  <text class="page-no" x="372" y="213">37</text>
  <text class="slide-title" x="17" y="31">Key Points Area</text>
  <text class="lorem" x="24" y="69">Lorem ipsum dolor sit amet, consectetur adipiscing elit, sed do eiusmod tempor incididunt ut labore et dolore magna aliqua. Ut enimad</text>
  <text class="lorem" x="24" y="76">minim veniam, quis nostrud exercitation ullamco laboris nisi ut aliquip ex ea commodo consequat.</text>
  <circle cx="101" cy="122" r="27" fill="var(--orange)"/>
  <circle cx="149" cy="122" r="27" fill="var(--green)"/>
  <circle cx="196" cy="122" r="27" fill="var(--blue)"/>
  <circle cx="243" cy="122" r="27" fill="var(--green)"/>
  <circle cx="290" cy="122" r="27" fill="var(--gold)"/>
  <use href="#i-people" x="94" y="108" width="14" height="14" color="#fff"/>
  <use href="#i-pen" x="143" y="109" width="12" height="12" color="#fff"/>
  <use href="#i-bars" x="190" y="109" width="12" height="12" color="#fff"/>
  <use href="#i-heart" x="237" y="109" width="12" height="12" color="#fff"/>
  <use href="#i-crown" x="284" y="109" width="12" height="12" color="#fff"/>
  <text class="lorem-w mid" x="101" y="129">Lorem</text><text class="lorem-w mid" x="101" y="134">ipsum</text>
  <text class="lorem-w mid" x="149" y="129">Lorem</text><text class="lorem-w mid" x="149" y="134">ipsum</text>
  <text class="lorem-w mid" x="196" y="129">Lorem</text><text class="lorem-w mid" x="196" y="134">ipsum</text>
  <text class="lorem-w mid" x="243" y="129">Lorem</text><text class="lorem-w mid" x="243" y="134">ipsum</text>
  <text class="lorem-w mid" x="290" y="129">Lorem</text><text class="lorem-w mid" x="290" y="134">ipsum</text>
  <text class="lorem mid" x="199" y="167">Lorem ipsum dolor sit amet, consectetur adipiscing elit, sed do eiusmod tempor incididunt ut labore</text>
  <text class="lorem mid" x="199" y="174">et dolore magna aliqua. Ut enimad minim veniam, quis nostrud exercitation ullamco laboris nisi ut</text>
  <text class="lorem mid" x="199" y="181">aliquip ex ea commodo consequat.</text>
</svg>

<!-- 8 Workflow -->
<svg class="slide col-2 row-3" viewBox="0 0 392 220">
  <use href="#slide-head"/><use href="#slide-foot"/>
  <text class="page-no" x="372" y="213">38</text>
  <text class="slide-title" x="17" y="31">Workflow Area</text>
  <text class="lorem" x="30" y="64">Lorem ipsum dolor sit amet, consectetur adipiscing elit, sed do eiusmod tempor incididunt ut labore et dolore magna aliqua. Ut enimad</text>
  <text class="lorem" x="30" y="71">minim veniam, quis nostrud exercitation ullamco laboris nisi ut aliquip ex ea commodo consequat.</text>
  <g fill="none" stroke-width="9">
    <path d="M33 134A33 33 0 0 1 99 134" stroke="var(--ink)"/>
    <path d="M99 134A33 33 0 0 0 165 134" stroke="var(--green)"/>
    <path d="M165 134A33 33 0 0 1 231 134" stroke="var(--ink)"/>
    <path d="M231 134A33 33 0 0 0 297 134" stroke="var(--green)"/>
    <path d="M297 134A33 33 0 0 1 363 134" stroke="var(--ink)"/>
  </g>
  <circle cx="66" cy="123" r="4.5" fill="var(--ink)"/><text class="tiny-w" x="66" y="124">1</text>
  <circle cx="198" cy="123" r="4.5" fill="var(--ink)"/><text class="tiny-w" x="198" y="124">3</text>
  <circle cx="330" cy="123" r="4.5" fill="var(--ink)"/><text class="tiny-w" x="330" y="124">5</text>
  <circle cx="132" cy="141" r="4.5" fill="var(--green-soft)"/><text class="tiny-w" x="132" y="142">2</text>
  <circle cx="264" cy="141" r="4.5" fill="var(--green-soft)"/><text class="tiny-w" x="264" y="142">4</text>
  <text class="label-b mid" x="66" y="139">Data 1</text>
  <text class="label-b mid" x="198" y="139">Data 3</text>
  <text class="label-b mid" x="330" y="139">Data 5</text>
  <text class="label mid c-green" x="132" y="94">Data 2</text>
  <text class="label mid c-green" x="264" y="94">Data 4</text>
  <g>
    <text class="lorem mid" x="132" y="101">Lorem ipsum dolor</text><text class="lorem mid" x="132" y="106">sit amet</text><text class="lorem mid" x="132" y="111">consectetur</text><text class="lorem mid" x="132" y="116">adipiscing elit</text>
    <text class="lorem mid" x="264" y="101">Lorem ipsum dolor</text><text class="lorem mid" x="264" y="106">sit amet</text><text class="lorem mid" x="264" y="111">consectetur</text><text class="lorem mid" x="264" y="116">adipiscing elit</text>
    <text class="lorem mid" x="66" y="148">Lorem ipsum dolor</text><text class="lorem mid" x="66" y="153">sit amet</text><text class="lorem mid" x="66" y="158">consectetur</text><text class="lorem mid" x="66" y="163">adipiscing elit</text>
    <text class="lorem mid" x="198" y="148">Lorem ipsum dolor</text><text class="lorem mid" x="198" y="153">sit amet</text><text class="lorem mid" x="198" y="158">consectetur</text><text class="lorem mid" x="198" y="163">adipiscing elit</text>
    <text class="lorem mid" x="330" y="148">Lorem ipsum dolor</text><text class="lorem mid" x="330" y="153">sit amet</text><text class="lorem mid" x="330" y="158">consectetur</text><text class="lorem mid" x="330" y="163">adipiscing elit</text>
  </g>
</svg>

<!-- 9 Timeline -->
<svg class="slide col-3 row-3" viewBox="0 0 392 220">
  <use href="#slide-head"/><use href="#slide-foot"/>
  <text class="page-no" x="372" y="213">39</text>
  <text class="slide-title" x="17" y="31">Timeline</text>
  <g stroke="#bdbdbd" stroke-width=".8">
    <line x1="52" y1="101" x2="334" y2="101"/>
    <line x1="100" y1="82" x2="100" y2="101"/><line x1="194" y1="82" x2="194" y2="101"/><line x1="287" y1="82" x2="287" y2="101"/>
    <line x1="147" y1="101" x2="147" y2="119"/><line x1="240" y1="101" x2="240" y2="119"/>
  </g>
  <g fill="#888"><circle cx="100" cy="101" r="1.2"/><circle cx="147" cy="101" r="1.2"/><circle cx="194" cy="101" r="1.2"/><circle cx="240" cy="101" r="1.2"/><circle cx="287" cy="101" r="1.2"/></g>
  <circle cx="52" cy="100" r="20" fill="var(--ink)"/><text class="year" x="52" y="101">2010</text><text class="tiny-w" x="52" y="106">Your Text</text><text class="tiny-w" x="52" y="109">Goes Here</text>
  <circle cx="100" cy="63" r="19" fill="var(--green-soft)"/><text class="year" x="100" y="65">2011</text><text class="tiny-w" x="100" y="70">Your Text</text><text class="tiny-w" x="100" y="73">Goes Here</text>
  <circle cx="147" cy="138" r="19" fill="var(--blue)"/><text class="year" x="147" y="140">2012</text><text class="tiny-w" x="147" y="145">Your Text</text><text class="tiny-w" x="147" y="148">Goes Here</text>
  <circle cx="194" cy="63" r="19" fill="var(--gold)"/><text class="year" x="194" y="65">2013</text><text class="tiny-w" x="194" y="70">Your Text</text><text class="tiny-w" x="194" y="73">Goes Here</text>
  <circle cx="240" cy="138" r="19" fill="var(--blue)"/><text class="year" x="240" y="140">2014</text><text class="tiny-w" x="240" y="145">Your Text</text><text class="tiny-w" x="240" y="148">Goes Here</text>
  <circle cx="287" cy="63" r="19" fill="var(--green-soft)"/><text class="year" x="287" y="65">2015</text><text class="tiny-w" x="287" y="70">Your Text</text><text class="tiny-w" x="287" y="73">Goes Here</text>
  <circle cx="334" cy="98" r="20" fill="var(--ink)"/><text class="year" x="334" y="100">2016</text><text class="tiny-w" x="334" y="105">Your Text</text><text class="tiny-w" x="334" y="108">Goes Here</text>
  <path d="M335 128q4 4-2 10" fill="none" stroke="#888" stroke-width=".6"/>
  <text class="label mid" x="321" y="145">Your Text Goes Here</text>
  <text class="lorem mid" x="321" y="151">Lorem ipsum dolor sit amet</text>
  <text class="lorem mid" x="321" y="156">consectetur adipiscing elit, sed</text>
  <text class="lorem mid" x="321" y="161">do eiusmod tempor incididunt</text>
  <text class="lorem mid" x="321" y="166">ut labore dolore magna</text>
  <text class="label" x="17" y="179">Your Text Goes Here</text>
  <text class="lorem" x="17" y="185">Lorem ipsum dolor sit amet, consectetur adipiscing elit, sed do eiusmod tempor</text>
  <text class="lorem" x="17" y="190">incididunt ut labore et dolore magna aliqua.</text>
</svg>

<!-- 10 Our Team -->
<svg class="slide col-1 row-4" viewBox="0 0 392 220">
  <use href="#slide-head"/><use href="#slide-foot"/>
  <text class="page-no" x="372" y="213">40</text>
  <text class="slide-title" x="17" y="31">Our Team</text>
  <circle cx="46" cy="75" r="19" fill="url(#photo-portrait)" role="img" aria-label="Portrait photo of Michael Doe"/>
  <circle cx="221" cy="75" r="19" fill="url(#photo-portrait)" role="img" aria-label="Portrait photo of James Doe"/>
  <circle cx="49" cy="146" r="19" fill="url(#photo-portrait)" role="img" aria-label="Portrait photo of Jane Doe"/>
  <circle cx="221" cy="146" r="19" fill="url(#photo-portrait)" role="img" aria-label="Portrait photo of John Doe"/>
  <g>
    <text class="label" x="74" y="68" style="font-size:5.8px">Michael Doe</text>
    <text class="lorem" x="74" y="74" style="fill:#333">CEO</text>
    <text class="lorem c-green" x="74" y="79">MS/MPh, MBA and CMA Gq PM</text>
    <text class="lorem" x="79" y="85">• Lorem ipsum dolor sit amet, consectetur</text>
    <text class="lorem" x="81" y="90">adipiscing elit</text>
    <text class="lorem" x="79" y="95">• sed do eiusmod tempor incididunt ut labore et</text>
    <text class="lorem" x="81" y="100">dolore magna aliqua.</text>
    <text class="lorem" x="79" y="105">• Ut enimad minim veniam, quis nostrud</text>
    <text class="lorem" x="81" y="110">exercitation</text>
  </g>
  <g>
    <text class="label" x="246" y="68" style="font-size:5.8px">James Doe</text>
    <text class="lorem" x="246" y="74" style="fill:#333">MANAGER</text>
    <text class="lorem c-green" x="246" y="79">M.B.A</text>
    <text class="lorem" x="251" y="85">• Lorem ipsum dolor sit amet, consectetur</text>
    <text class="lorem" x="253" y="90">adipiscing elit</text>
    <text class="lorem" x="251" y="95">• sed do eiusmod tempor incididunt ut labore et</text>
    <text class="lorem" x="253" y="100">dolore magna aliqua.</text>
    <text class="lorem" x="251" y="105">• Ut enimad minim veniam, quis nostrud</text>
    <text class="lorem" x="253" y="110">exercitation</text>
  </g>
  <g>
    <text class="label" x="73" y="143" style="font-size:5.8px">Jane Doe</text>
    <text class="lorem" x="73" y="149" style="fill:#333">Doctor of Chemistry</text>
    <text class="lorem c-green" x="73" y="154">M.B.A</text>
    <text class="lorem" x="78" y="160">• Lorem ipsum dolor sit amet, consectetur</text>
    <text class="lorem" x="80" y="165">adipiscing elit</text>
    <text class="lorem" x="78" y="170">• sed do eiusmod tempor incididunt ut labore et</text>
    <text class="lorem" x="80" y="175">dolore magna aliqua.</text>
    <text class="lorem" x="78" y="180">• Ut enimad minim veniam, quis nostrud</text>
    <text class="lorem" x="80" y="185">exercitation</text>
  </g>
  <g>
    <text class="label" x="246" y="143" style="font-size:5.8px">John Doe</text>
    <text class="lorem" x="246" y="149" style="fill:#333">Doctor of Physical</text>
    <text class="lorem c-green" x="246" y="154">Professor</text>
    <text class="lorem" x="251" y="160">• Lorem ipsum dolor sit amet, consectetur</text>
    <text class="lorem" x="253" y="165">adipiscing elit</text>
    <text class="lorem" x="251" y="170">• sed do eiusmod tempor incididunt ut labore et</text>
    <text class="lorem" x="253" y="175">dolore magna aliqua.</text>
    <text class="lorem" x="251" y="180">• Ut enimad minim veniam, quis nostrud</text>
    <text class="lorem" x="253" y="185">exercitation</text>
  </g>
</svg>

<!-- 11 Customer Testimonials -->
<svg class="slide col-2 row-4" viewBox="0 0 392 220">
  <use href="#slide-head"/>
  <text class="slide-title" x="17" y="31">Customer Testimonials</text>
  <circle cx="111" cy="74" r="27" fill="#f0f0f0"/>
  <circle cx="111" cy="74" r="25" fill="url(#photo-portrait)" role="img" aria-label="Portrait photo of a client"/>
  <text class="lorem" x="168" y="67">adipiscing elit, sed diam nonummy nibh euismod tincidunt ut</text>
  <text class="lorem" x="168" y="73">laoreet dolore magna aliquam erat volutpat. Ut wisi enim <tspan style="fill:#333;font-weight:600">Lorem</tspan></text>
  <text class="lorem" x="168" y="79"><tspan style="fill:#333;font-weight:600">ipsum</tspan> dolor sit amet, consectetuer adipiscing elit, sed diam</text>
  <text class="lorem" x="168" y="85">nonummy nibh euismod tincidunt ut laoreet dolore magna</text>
  <rect x="0" y="118" width="392" height="102" fill="url(#band-green-blue)"/>
  <path d="M106 118l5-5 5 5z" fill="var(--green)"/>
  <g fill="none" stroke="#fff" stroke-width=".8">
    <circle cx="93" cy="153" r="14"/><circle cx="167" cy="153" r="14"/><circle cx="241" cy="153" r="14"/><circle cx="317" cy="153" r="14"/>
  </g>
  <use href="#i-search" x="88" y="148" width="10" height="10" color="#fff"/>
  <use href="#i-box" x="162" y="148" width="10" height="10" color="#fff"/>
  <use href="#i-bars" x="236" y="148" width="10" height="10" color="#fff"/>
  <use href="#i-box" x="312" y="148" width="10" height="10" color="#fff"/>
  <g>
    <text class="lorem-w mid" x="93" y="179">Why does getting a loan</text><text class="lorem-w mid" x="93" y="184">have to be so much more</text><text class="lorem-w mid" x="93" y="189">complicated than ordering</text><text class="lorem-w mid" x="93" y="194">a fridge on the web?</text>
    <text class="lorem-w mid" x="167" y="179">Why do I have to go to</text><text class="lorem-w mid" x="167" y="184">a branch, fill out forms</text><text class="lorem-w mid" x="167" y="189">and wait for weeks to</text><text class="lorem-w mid" x="167" y="194">get a response?</text>
    <text class="lorem-w mid" x="241" y="179">Why do banks refuse</text><text class="lorem-w mid" x="241" y="184">to lend to me despite</text><text class="lorem-w mid" x="241" y="189">the substantial fees I</text><text class="lorem-w mid" x="241" y="194">receive each month?</text>
    <text class="lorem-w mid" x="317" y="179">Why is there no service</text><text class="lorem-w mid" x="317" y="184">in banking that identifies</text><text class="lorem-w mid" x="317" y="189">my needs and offers</text><text class="lorem-w mid" x="317" y="194">convenience at fair prices?</text>
  </g>
</svg>

<!-- 12 Bullet & Chart (bars) -->
<svg class="slide col-3 row-4" viewBox="0 0 392 220">
  <use href="#slide-head"/><use href="#slide-foot"/>
  <text class="page-no" x="372" y="213">42</text>
  <text class="slide-title" x="17" y="31">Bullet &amp; Chart Area</text>
  <line x1="55" y1="64" x2="55" y2="175" stroke="#ddd" stroke-width=".5"/>
  <g>
    <text class="lorem end" x="52" y="78">Category 4</text>
    <rect x="56" y="69" width="108" height="4" fill="var(--blue)"/><rect x="56" y="74" width="84" height="4" fill="var(--green)"/><rect x="56" y="79" width="97" height="4" fill="var(--ink)"/>
    <text class="lorem end" x="52" y="106">Category 3</text>
    <rect x="56" y="97" width="58" height="4" fill="var(--blue)"/><rect x="56" y="102" width="48" height="4" fill="var(--green)"/><rect x="56" y="107" width="76" height="4" fill="var(--ink)"/>
    <text class="lorem end" x="52" y="134">Category 2</text>
    <rect x="56" y="125" width="42" height="4" fill="var(--blue)"/><rect x="56" y="130" width="95" height="4" fill="var(--green)"/><rect x="56" y="135" width="70" height="4" fill="var(--ink)"/>
    <text class="lorem end" x="52" y="162">Category 1</text>
    <rect x="56" y="153" width="50" height="4" fill="var(--blue)"/><rect x="56" y="158" width="42" height="4" fill="var(--green)"/><rect x="56" y="163" width="86" height="4" fill="var(--ink)"/>
  </g>
  <rect x="78" y="183" width="2.5" height="2.5" fill="var(--blue)"/><text class="lorem" x="82" y="185.5">Series 3</text>
  <rect x="98" y="183" width="2.5" height="2.5" fill="var(--green)"/><text class="lorem" x="102" y="185.5">Series 2</text>
  <rect x="118" y="183" width="2.5" height="2.5" fill="var(--ink)"/><text class="lorem" x="122" y="185.5">Series 1</text>
  <circle cx="221" cy="73" r="7.5" fill="var(--ink)"/><use href="#i-search" x="217" y="69" width="8" height="8" color="#fff"/>
  <circle cx="221" cy="105" r="7.5" fill="var(--green)"/><use href="#i-pen" x="217" y="101" width="8" height="8" color="#fff"/>
  <circle cx="221" cy="137" r="7.5" fill="var(--ink)"/><use href="#i-pen" x="217" y="133" width="8" height="8" color="#fff"/>
  <circle cx="221" cy="169" r="7.5" fill="var(--green)"/><use href="#i-gear" x="217" y="165" width="8" height="8" color="#fff"/>
  <text class="label" x="239" y="72">Category One</text><text class="lorem" x="239" y="78">Lorem ipsum dolor sit amet, consectetur adipiscing</text><text class="lorem" x="239" y="83">elit, sed do eiusmod</text>
  <text class="label c-green" x="239" y="104">Category Two</text><text class="lorem" x="239" y="110">Lorem ipsum dolor sit amet, consectetur adipiscing</text><text class="lorem" x="239" y="115">elit, sed do eiusmod</text>
  <text class="label" x="239" y="136">Category Three</text><text class="lorem" x="239" y="142">Lorem ipsum dolor sit amet, consectetur adipiscing</text><text class="lorem" x="239" y="147">elit, sed do eiusmod</text>
  <text class="label c-green" x="239" y="168">Category Four</text><text class="lorem" x="239" y="174">Lorem ipsum dolor sit amet, consectetur adipiscing</text><text class="lorem" x="239" y="179">elit, sed do eiusmod</text>
</svg>

<!-- 13 Table -->
<svg class="slide col-1 row-5" viewBox="0 0 392 220">
  <use href="#slide-head"/><use href="#slide-foot"/>
  <text class="page-no" x="372" y="213">43</text>
  <text class="slide-title" x="17" y="31">Table Area</text>
  <rect x="59" y="55" width="112" height="35" fill="var(--ink)"/>
  <rect x="171" y="55" width="80" height="35" fill="var(--blue)"/>
  <rect x="251" y="55" width="84" height="35" fill="var(--green)"/>
  <rect x="59" y="90" width="276" height="96" fill="#fff" stroke="#eeeeee" stroke-width=".6"/>
  <text class="label on-dark" x="66" y="74">Description</text>
  <text class="label on-dark mid" x="211" y="69">Column 1</text>
  <text class="label on-dark mid" x="293" y="69">Column 2</text>
  <circle cx="211" cy="85" r="6" fill="#fff"/><use href="#i-pen" x="207" y="81" width="8" height="8" color="var(--blue)"/>
  <circle cx="293" cy="85" r="6" fill="#fff"/><use href="#i-crown" x="289" y="81" width="8" height="8" color="var(--green)"/>
  <g stroke="#e4e4e4" stroke-width=".5">
    <line x1="66" y1="113" x2="164" y2="113"/><line x1="177" y1="113" x2="245" y2="113"/><line x1="258" y1="113" x2="328" y2="113"/>
    <line x1="66" y1="121.5" x2="164" y2="121.5"/><line x1="177" y1="121.5" x2="245" y2="121.5"/><line x1="258" y1="121.5" x2="328" y2="121.5"/>
    <line x1="66" y1="130" x2="164" y2="130"/><line x1="177" y1="130" x2="245" y2="130"/><line x1="258" y1="130" x2="328" y2="130"/>
    <line x1="66" y1="138.5" x2="164" y2="138.5"/><line x1="177" y1="138.5" x2="245" y2="138.5"/><line x1="258" y1="138.5" x2="328" y2="138.5"/>
    <line x1="66" y1="147" x2="164" y2="147"/><line x1="177" y1="147" x2="245" y2="147"/><line x1="258" y1="147" x2="328" y2="147"/>
    <line x1="66" y1="155.5" x2="164" y2="155.5"/><line x1="177" y1="155.5" x2="245" y2="155.5"/><line x1="258" y1="155.5" x2="328" y2="155.5"/>
    <line x1="66" y1="164" x2="164" y2="164"/><line x1="177" y1="164" x2="245" y2="164"/><line x1="258" y1="164" x2="328" y2="164"/>
    <line x1="66" y1="172.5" x2="164" y2="172.5"/><line x1="177" y1="172.5" x2="245" y2="172.5"/><line x1="258" y1="172.5" x2="328" y2="172.5"/>
  </g>
  <g>
    <text class="lorem" x="67" y="111" style="fill:#555">Description 1</text>
    <text class="lorem" x="67" y="119.5" style="fill:#555">Description 2</text>
    <text class="lorem" x="67" y="128" style="fill:#555">Description 3</text>
    <text class="lorem" x="67" y="136.5" style="fill:#555">Description 4</text>
    <text class="lorem" x="67" y="145" style="fill:#555">Description 5</text>
    <text class="lorem" x="67" y="153.5" style="fill:#555">Description 6</text>
    <text class="lorem" x="67" y="162" style="fill:#555">Description 7</text>
    <text class="lorem" x="67" y="170.5" style="fill:#555">Description 8</text>
  </g>
  <g fill="var(--ink)">
    <circle cx="293" cy="110" r="1.3"/>
    <circle cx="211" cy="118.5" r="1.3"/><circle cx="293" cy="118.5" r="1.3"/>
    <circle cx="211" cy="127" r="1.3"/><circle cx="293" cy="127" r="1.3"/>
    <circle cx="293" cy="135.5" r="1.3"/>
    <circle cx="211" cy="153" r="1.3"/><circle cx="293" cy="153" r="1.3"/>
    <circle cx="211" cy="169.5" r="1.3"/><circle cx="293" cy="169.5" r="1.3"/>
  </g>
  <text class="lorem mid" x="211" y="145" style="fill:#333">Text Column 1</text><text class="lorem mid" x="293" y="145" style="fill:#333">Text Column 2</text>
  <text class="lorem mid" x="211" y="162" style="fill:#333">Text Column 1</text><text class="lorem mid" x="293" y="162" style="fill:#333">Text Column 2</text>
</svg>

<!-- 14 Bullet & Chart (donut) -->
<svg class="slide col-2 row-5" viewBox="0 0 392 220">
  <use href="#slide-head"/><use href="#slide-foot"/>
  <text class="page-no" x="372" y="213">44</text>
  <text class="slide-title" x="17" y="31">Bullet &amp; Chart Area</text>
  <circle cx="47" cy="72" r="7.5" fill="var(--ink)"/><use href="#i-search" x="43" y="68" width="8" height="8" color="#fff"/>
  <circle cx="47" cy="104" r="7.5" fill="var(--green)"/><use href="#i-tick" x="43" y="100" width="8" height="8" color="#fff"/>
  <circle cx="47" cy="136" r="7.5" fill="#c4c4c4"/><use href="#i-pen" x="43" y="132" width="8" height="8" color="#fff"/>
  <circle cx="47" cy="170" r="7.5" fill="#9a9a9a"/><use href="#i-gear" x="43" y="166" width="8" height="8" color="#fff"/>
  <text class="label" x="65" y="71">Your Text Here</text><text class="lorem" x="65" y="78">Lorem ipsum dolor sit amet, consectetur adipiscing</text><text class="lorem" x="65" y="83">elit, sed do eiusmod</text>
  <text class="label c-green" x="65" y="103">Your Text Here</text><text class="lorem" x="65" y="110">Lorem ipsum dolor sit amet, consectetur adipiscing</text><text class="lorem" x="65" y="115">elit, sed do eiusmod</text>
  <text class="label" x="65" y="135" style="fill:#bbb">Your Text Here</text><text class="lorem" x="65" y="142">Lorem ipsum dolor sit amet, consectetur adipiscing</text><text class="lorem" x="65" y="147">elit, sed do eiusmod</text>
  <text class="label" x="65" y="168">Your Text Here</text><text class="lorem" x="65" y="175">Lorem ipsum dolor sit amet, consectetur adipiscing</text><text class="lorem" x="65" y="180">elit, sed do eiusmod</text>
  <g fill="none" stroke-width="13" transform="rotate(-90 282 123)">
    <circle cx="282" cy="123" r="38" stroke="var(--ink)" stroke-dasharray="131.3 238.8"/>
    <circle cx="282" cy="123" r="38" stroke="var(--green)" stroke-dasharray="59.7 238.8" stroke-dashoffset="-131.3"/>
    <circle cx="282" cy="123" r="38" stroke="#dcdcdc" stroke-dasharray="28.7 238.8" stroke-dashoffset="-191"/>
    <circle cx="282" cy="123" r="38" stroke="#8a8a8a" stroke-dasharray="19.1 238.8" stroke-dashoffset="-219.7"/>
  </g>
  <use href="#i-bars" x="270" y="110" width="24" height="24" color="#8a8a8a"/>
  <text class="pct" x="250" y="68">10%</text>
  <text class="pct" x="212" y="99">15%</text>
  <text class="pct" x="212" y="153">25%</text>
  <text class="pct" x="336" y="126" style="fill:#333">60%</text>
  <circle cx="245" cy="178.5" r="1.2" fill="var(--ink)"/><text class="lorem" x="247.5" y="180">1st Qtr</text>
  <circle cx="263" cy="178.5" r="1.2" fill="var(--green)"/><text class="lorem" x="265.5" y="180">2nd Qtr</text>
  <circle cx="282" cy="178.5" r="1.2" fill="#dcdcdc"/><text class="lorem" x="284.5" y="180">3rd Qtr</text>
  <circle cx="300" cy="178.5" r="1.2" fill="#8a8a8a"/><text class="lorem" x="302.5" y="180">4th Qtr</text>
</svg>

<!-- 15 Contact / Thank you -->
<svg class="slide col-3 row-5" viewBox="0 0 392 220">
  <rect x="0" y="0" width="392" height="220" fill="url(#photo-contact)" role="img" aria-label="Photo of pencils on a desk, tinted green to teal"/>
  <rect x="39" y="0" width="136" height="220" fill="#8cc63f" opacity=".95"/>
  <rect x="39" y="198" width="136" height="22" fill="var(--blue)"/>
  <rect x="63" y="28" width="10" height="10" fill="#fff"/>
  <text class="brand" x="77" y="36" style="fill:#fff">BOLD KETTLE WORKS</text>
  <text class="big-w" x="53" y="89" style="font-size:12px">Our Contact</text>
  <path d="M56 112.5a2 2 0 1 1 4 0c0 1.6-2 3.8-2 3.8s-2-2.2-2-3.8z" fill="#fff"/>
  <text class="lorem-w" x="67" y="115" style="font-size:3.6px">123 Street Road</text>
  <text class="lorem-w" x="67" y="120" style="font-size:3.6px">City 12345</text>
  <path d="M56 130.5l1.4-.8 1 1.6-.8.6c.4 1 1 1.7 2 2.1l.6-.8 1.6 1-.8 1.4c-2.6-.4-4.6-2.4-5-5.1z" fill="#fff"/>
  <text class="lorem-w" x="67" y="134" style="font-size:3.6px">(123) 456-7890</text>
  <rect x="56" y="148" width="5" height="3.6" fill="#fff"/>
  <text class="lorem-w" x="67" y="151.5" style="font-size:3.6px">emailaddress@email.com</text>
  <circle cx="58.5" cy="167" r="2.3" fill="none" stroke="#fff" stroke-width=".8"/>
  <text class="lorem-w" x="67" y="168.5" style="font-size:3.6px">www.website-address.com</text>
  <circle cx="90" cy="209" r="4.5" fill="#fff"/>
  <circle cx="106" cy="209" r="4.5" fill="#fff"/>
  <circle cx="122" cy="209" r="4.5" fill="#fff"/>
  <text class="big-w" x="283" y="134" style="font-size:15px;text-anchor:middle">THANK YOU</text>
  <text class="big-w" x="283" y="144" style="font-size:5px;text-anchor:middle;fill:#c9e86c">For Your Precious Time</text>
  <text class="lorem-w mid" x="283" y="160" style="font-size:4.2px">Stop by our office or give us a call</text>
  <text class="lorem-w mid" x="283" y="166" style="font-size:4.2px">We would love to hear from you.</text>
</svg>

</body>
</html>
```